I need to launch a new website that more accurately reflects what we do as a business. We are an IT Reseller that specialises in delivering innovative solutions covering supply, implementation and support. My current website is www.vornetikx.com and was something I designed myself on the Hub Nimbo website. This was fine for the first 2 years but now I need something more professional and detailed. A couple of websites for companies similar to Brindle KTR are www.quarvolen.co.uk and www.ferrimund.co.uk. By looking at these it will hopefully give you an idea as to what I am trying to achieve.

Target Market(s)

UK based companies with between 30-250 employees, no fixed vertical

Coding

Coded - Design and coding required

Number of Pages Required

4 page

Font styles to use
Sans Serif

Colors
33a6d7
0592cd
85cae6

Requirements
Must have
• Contact details page to include a "Get in touch with us " section, About Us page, IT Support page to include the headings 1/ Proactive Monitoring 2/ 24 x 7 Support 3/ Security and Data Back-up 4/ Built-in Compliance (GDPR) 5/ Responsive IT Support. I am happy to provide the wording for these headings.
Clean crisp home screen with a Menu offering the requested drop down options.
Nice to have
• Easy to navigate site with a good flow. I have updated a page regarding cloud services, this would be great to have as a separate drop down menu option. I would like to have different Cloud logo's in ideally the Brindle Blue colour. Can you please add the photograph of Thornwick Lodge which is my office in the contact us page.
Should not have
• I definitely DO NOT want a photo/view of London on the home page!!

```html
<!DOCTYPE html>
<html lang="en">
<head>
<meta charset="utf-8">
<title>Brindle KTR — IT Reseller</title>
<link rel="stylesheet" href="https://fonts.googleapis.com/css2?family=Montserrat:wght@400;500;600&family=Arimo:wght@400&display=swap">
<style>
:root{
  --blue:#1f86c9;
  --blue-bright:#2b91d0;
  --blue-light:#85cae6;
  --ink:#2b2b2b;
  --text:#555;
  --grey-bg:#eceef1;
  --footer:#232323;
  --white:#fff;
}
*{box-sizing:border-box;margin:0;padding:0}
html,body{width:1200px;height:3485px;overflow:hidden}
body{position:relative;background:var(--white);font-family:"Montserrat",sans-serif;color:var(--ink)}
.abs{position:absolute}
.body-copy{font-family:"Arimo",sans-serif;color:var(--text)}

/* header */
.site-header{top:0;left:0;width:1200px;height:133px;background:var(--white)}
.brand{display:flex;align-items:center;gap:14px;left:112px;top:40px}
.brand-mark{width:40px;height:40px;border-radius:50%;background:var(--blue)}
.brand-name{font-size:24px;font-weight:500;color:var(--ink)}
.main-nav{top:60px;left:467px;display:flex;gap:40px;font-size:15px;font-weight:500;letter-spacing:.2px}
.main-nav span{color:#222}
.main-nav .active{color:var(--blue)}

/* hero */
.hero{top:133px;left:0;width:1200px;height:691px;background:linear-gradient(110deg,#0e1c2a 0%,#1d3a55 30%,#283848 55%,#151d27 80%,#0d1219 100%)}
.hero-title{left:735px;top:305px;font-size:80px;font-weight:500;color:var(--blue-bright);letter-spacing:1px}
.hero-lead{left:743px;top:422px;width:420px;font-size:24px;line-height:40.5px;color:var(--white)}

/* contact form */
.contact-card{left:718px;top:702px;width:371px;height:575px;background:var(--white);box-shadow:0 2px 8px rgba(0,0,0,.08)}
.contact-card svg{position:absolute;left:0;top:0}
.contact-title{position:absolute;left:0;top:28px;width:100%;text-align:center;color:var(--white);font-size:20px;font-weight:500}
.field{position:absolute;left:32px;width:309px;height:49px;border:1px solid #d7d7d7;border-radius:3px;box-shadow:0 1px 3px rgba(0,0,0,.08);font-family:"Arimo",sans-serif;font-size:13px;color:#444;padding:17px 14px}
.field.msg{height:126px}
.submit{position:absolute;left:32px;top:494px;width:309px;height:49px;background:var(--blue-bright);color:var(--white);font-size:18px;font-weight:500;text-align:center;line-height:49px;border-radius:2px}

/* welcome */
.welcome-title{left:112px;top:878px;font-size:38px;font-weight:500}
.accent{color:var(--blue)}
.rule{height:3px;background:var(--ink)}
.welcome-copy{left:112px;top:966px;width:550px;font-size:14px;line-height:25.7px;text-align:justify}
.btn{background:var(--blue);color:var(--white);font-weight:500;text-align:center;border-radius:2px}
.read-more{left:112px;top:1201px;width:165px;height:55px;line-height:55px;font-size:16px}

/* it support */
.support{top:1345px;left:0;width:1200px;height:590px;background:linear-gradient(180deg,#f1f3f5,#e6e9ed)}
.section-title{width:1200px;left:0;text-align:center;font-weight:500}
.section-sub{width:1200px;left:0;text-align:center;font-size:15px}
.service{top:1514px;width:234px;height:348px;background:var(--white);border:1px solid #e2e2e2;box-shadow:0 1px 4px rgba(0,0,0,.08);text-align:center}
.service .photo{margin:4px;height:171px}
.service h3{font-size:16px;font-weight:500;line-height:24px;margin-top:18px;color:#222}
.service p{font-size:14px;line-height:25px;margin-top:8px;padding:0 18px}
.dots{top:1896px;left:577px;display:flex;gap:8px}
.dots i{width:11px;height:11px;border-radius:50%;background:#b9bec4}
.dots i.on{background:var(--blue)}

/* banner */
.banner{top:1935px;left:0;width:1200px;height:521px;background:linear-gradient(180deg,#2079c0 0%,#256fb0 45%,#3f7fb8 70%,#2c78c0 100%)}
.banner-kicker{top:2090px;font-size:32px;color:var(--white)}
.banner-title{top:2140px;font-size:40px;font-weight:500;color:var(--white);letter-spacing:.5px}
.banner-btn{left:440px;top:2222px;width:320px;height:65px;border:2px solid var(--white);border-radius:33px;color:var(--white);font-size:17px;font-weight:500;text-align:center;line-height:61px}

/* blog */
.post-photo{top:2632px;width:315px;height:277px}
.post{top:2855px;width:283px;height:216px;background:var(--white);box-shadow:0 1px 5px rgba(0,0,0,.12);text-align:center}
.post .date{margin-top:30px;font-size:16px;color:var(--blue);font-weight:500}
.post h4{margin-top:16px;font-size:15px;font-weight:600;line-height:23px;color:#222}
.post p{margin-top:10px;font-size:14px;line-height:25.5px;padding:0 20px}

/* footer */
.site-footer{top:3138px;left:0;width:1200px;height:347px;background:var(--footer)}
.footer-brand{left:448px;top:3198px;display:flex;align-items:center;gap:18px}
.footer-brand .brand-mark{width:52px;height:52px;background:var(--white)}
.footer-brand .brand-name{color:var(--white);font-size:32px}
.footer-nav{top:3298px;left:0;width:1200px;display:flex;justify-content:center;gap:46px;font-size:15px;font-weight:500;color:var(--white)}
.social{top:3355px;left:0;width:1200px;display:flex;justify-content:center;gap:6px}
.social i{width:35px;height:35px;border:2px solid var(--white);border-radius:50%}
.copyright{top:3417px;font-size:14px;color:var(--white)}
</style>
</head>
<body>

<header class="abs site-header">
  <div class="abs brand"><span class="brand-mark"></span><span class="brand-name">Brindle KTR</span></div>
  <nav class="abs main-nav">
    <span class="active">HOME</span><span>ABOUT US</span><span>SERVICES</span><span>IT SUPPORT</span><span>BLOG</span><span>CONTACT US</span>
  </nav>
</header>

<section class="abs hero" role="img" aria-label="Support team wearing headsets working at monitors in a dark office"></section>
<div class="abs hero-title">Brindle</div>
<p class="abs hero-lead">IT Reseller that specialises in delivering innovative solutions covering supply, implementation and support.</p>

<aside class="abs contact-card">
  <svg width="371" height="90" viewBox="0 0 371 90"><path d="M0 0H371V70L255 87Q185 90 115 80L0 62Z" fill="#2b91d0"/></svg>
  <div class="contact-title">GET IN TOUCH WITH US</div>
  <div class="field" style="top:125px">First Name :</div>
  <div class="field" style="top:183px">Last Name :</div>
  <div class="field" style="top:240px">Email :</div>
  <div class="field" style="top:298px">Phone :</div>
  <div class="field msg" style="top:355px">Message :</div>
  <div class="submit">GET IN TOUCH</div>
</aside>

<h1 class="abs welcome-title">Welcome <span class="accent">Brindle</span></h1>
<div class="abs rule" style="left:112px;top:931px;width:52px"></div>
<p class="abs body-copy welcome-copy">Sed ut perspiciatis unde omnis iste natus error sit voluptatem accusantium doloremque laud antium, totam rem aperiam, eaque ipsa quae ab illo inventore veritatis et quasi architecto beatae vitae dicta sunt explicabo. Nemo enim ipsam voluptatem quia voluptas sit aspernat ur aut odit aut fugit, sed quia consequuntur magni dolores eos qui ratione voluptatem sequi nesciunt. Neque porro quisquam est, qui dolorem ipsum quia dolor sit amet, consectetur, adipisci velit, sed quia non numquam eius modi tempora incidunt ut labore et dolore magnam aliquam quaerat voluptatem. Ut enim ad minima veniam, quis nostrum exercita-tionem ullam corporis suscipit laboriosam, nisi ut aliquid...</p>
<div class="abs btn read-more">READ MORE</div>

<section class="abs support"></section>
<h2 class="abs section-title" style="top:1378px;font-size:43px">IT <span class="accent">Support</span></h2>
<p class="abs body-copy section-sub" style="top:1462px">Sed ut perspiciatis unde omnis iste natus error sit voluptatem accusantium doloremque</p>

<article class="abs service" style="left:111px">
  <div class="photo" role="img" aria-label="Laptop with a to-do checklist on screen and notes on a desk" style="background:linear-gradient(135deg,#c9b99a,#6d6a62)"></div>
  <h3>PROACTIVE<br>MONITORING</h3>
  <p class="body-copy">Sed ut perspiciatis unde omnis iste natus error sit voluptatem accusantium dolorem</p>
</article>
<article class="abs service" style="left:359px">
  <div class="photo" role="img" aria-label="Support agent with a headset at a help desk" style="background:linear-gradient(135deg,#d8d6d2,#8a8078)"></div>
  <h3>24 X 7<br>SUPPORT</h3>
  <p class="body-copy">Sed ut perspiciatis unde omnis iste natus error sit voluptatem accusantium dolorem</p>
</article>
<article class="abs service" style="left:606px">
  <div class="photo" role="img" aria-label="Hands on a laptop with a glowing security shield overlay" style="background:linear-gradient(135deg,#0f2a3c,#2a6f8c)"></div>
  <h3>SECURITY &amp;<br>DATA BACK-UP</h3>
  <p class="body-copy">Sed ut perspiciatis unde omnis iste natus error sit voluptatem accusantium dolorem</p>
</article>
<article class="abs service" style="left:854px">
  <div class="photo" role="img" aria-label="Compliance concept with hexagon icons for law, rules and audit" style="background:linear-gradient(135deg,#3a5f8a,#9bb0c6)"></div>
  <h3>BUILT-IN<br>COMPLIANCE</h3>
  <p class="body-copy">Sed ut perspiciatis unde omnis iste natus error sit voluptatem accusantium dolorem</p>
</article>
<div class="abs dots"><i></i><i class="on"></i><i></i></div>

<section class="abs banner" role="img" aria-label="City skyline and river at dusk under a blue tint"></section>
<p class="abs section-title banner-kicker">Sed ut perspiciatis unde</p>
<h2 class="abs section-title banner-title">ISTE NATUS ERROR SIT VOLUPTATEM</h2>
<div class="abs banner-btn">CLICK HERE FOR MORE INFO</div>

<h2 class="abs section-title" style="top:2494px;font-size:42px">LATEST <span class="accent">BLOG</span></h2>
<div class="abs" style="left:579px;top:2560px;width:42px;height:3px;background:var(--blue)"></div>
<p class="abs body-copy section-sub" style="top:2579px">Sed ut perspiciatis unde omnis iste natus error sit voluptatem accusantium doloremque</p>

<div class="abs post-photo" style="left:111px;background:linear-gradient(135deg,#3d3b38,#a79d90)" role="img" aria-label="Two colleagues reviewing work at a laptop"></div>
<div class="abs post-photo" style="left:443px;background:linear-gradient(135deg,#e8d9bd,#6e6a64)" role="img" aria-label="Hands pointing at charts on a meeting table"></div>
<div class="abs post-photo" style="left:774px;background:linear-gradient(135deg,#d9d7d3,#3b3f48)" role="img" aria-label="Business partners talking at a table"></div>

<article class="abs post" style="left:127px">
  <div class="date">OCTOBER 14, 2020</div>
  <h4>SED UT PERSPICIATIS UNDE<br>OMNIS ISTE NATUS</h4>
  <p class="body-copy">Nemo enim ipsam voluptatem quia voluptas sit aspernatur aut odit aut sed quia consequuntur</p>
</article>
<article class="abs post" style="left:459px">
  <div class="date">OCTOBER 14, 2020</div>
  <h4>SED UT PERSPICIATIS UNDE<br>OMNIS ISTE NATUS</h4>
  <p class="body-copy">Nemo enim ipsam voluptatem quia voluptas sit aspernatur aut odit aut sed quia consequuntur</p>
</article>
<article class="abs post" style="left:790px">
  <div class="date">OCTOBER 14, 2020</div>
  <h4>SED UT PERSPICIATIS UNDE<br>OMNIS ISTE NATUS</h4>
  <p class="body-copy">Nemo enim ipsam voluptatem quia voluptas sit aspernatur aut odit aut sed quia consequuntur</p>
</article>

<footer class="abs site-footer"></footer>
<div class="abs footer-brand"><span class="brand-mark"></span><span class="brand-name">Brindle KTR</span></div>
<nav class="abs footer-nav"><span>HOME</span><span>ABOUT US</span><span>SERVICES</span><span>IT SUPPORT</span><span>BLOG</span><span>CONTACT US</span></nav>
<div class="abs social" aria-label="Social links"><i></i><i></i><i></i><i></i><i></i></div>
<p class="abs section-title copyright">© Copyrights 2020-Brindle KTR.All Rights Reserved.</p>

</body>
</html>
```